New Joomla Website for Marquee Hire Co

We need a web design for our new Marquee Hire Co here in New Zealand called Brightfield Canopies.
We rather like the retro look, as it fit very well with the current trends in weddings that is a more of a retro look (and we had our logo designed to reflect that!). The 50's and 60's wedding styles are really making a comeback. We would like to communicate to that market effectively.

The Home page should have a slider image with space for a headline on it. It is a visual product we have (but we are selling that dream of a perfect wedding/party/event).

Our competition here have a really nice site that you could look at - www.plovane.co.nz

The other pages would have space for a picture, and then a blurb under each element related to it.
We will have a FAQ, Gallery, Hire and Contact us pages - we will add them as we go along.

From a technical perspective, we are using Joomla 2.5 and upwards.

Any questions - let me know. I look forward seeing the designs!

Target Market(s)

Couples looking for a wedding marquee, birthday parties, Corporate events

Industry/Entity Type

Wedding

Requirements
Must have
• 1. Preferably done in Joomla. I will also look at Wordpress site.
2. It has to have a retro look and feel.
3. It has to use my brand new logo (included)

```html
<!DOCTYPE html>
<html lang="en">
<head>
<meta charset="utf-8">
<title>Brightfield Canopies – Marquee Hire New Zealand</title>
<link rel="stylesheet" href="https://fonts.googleapis.com/css2?family=Lobster&family=Tinos&family=Didact+Gothic&family=Bebas+Neue&display=swap">
<style>
  :root {
    --paper: #f4f1ec;
    --brown: #5a3d24;
    --brown-dark: #47301c;
    --ink: #4a2e1a;
    --sky: #9fbde0;
    --sky-fill: #b4cfee;
    --teal-ring: #5b9ab5;
    --teal-text: #1e5a6e;
    --pink: #f1c6d0;
    --gold: #d8b45a;
    --gold-zig: #e7cf86;
    --line: #8a6a4f;
  }
  * { margin: 0; padding: 0; box-sizing: border-box; }
  html, body { width: 1200px; height: 1180px; overflow: hidden; }
  body { background: var(--paper); font-family: "Tinos", serif; color: var(--ink); position: relative; }

  .brand { position: absolute; left: 92px; top: 110px; display: flex; align-items: center; gap: 14px; }
  .brand-dot { width: 44px; height: 44px; border-radius: 50%; background: var(--sky); }
  .brand-name { font-family: "Lobster", cursive; font-size: 40px; color: var(--brown); white-space: nowrap; }

  .main-nav { position: absolute; left: 505px; top: 116px; display: flex; align-items: center; }
  .main-nav a { font-family: "Lobster", cursive; font-size: 28px; color: var(--sky); text-decoration: none; white-space: nowrap; }
  .main-nav a.is-current { color: var(--gold); }
  .main-nav .sep { width: 0; height: 0; border-left: 6px solid transparent; border-right: 6px solid transparent; border-bottom: 7px solid var(--sky); margin: 8px 16px 0; }

  .rule { position: absolute; left: 109px; width: 980px; height: 1px; background: var(--line); }

  .slider { position: absolute; left: 109px; top: 179px; width: 980px; height: 380px; overflow: hidden; }
  .slide-photo { position: absolute; left: 0; top: 0; width: 664px; height: 380px;
    background: linear-gradient(180deg, #5f7a45 0%, #a6ad93 28%, #e9e9e6 45%, #cfcac2 62%, #7a6a5a 85%, #6b5648 100%); }
  .slide-zig { position: absolute; left: 658px; top: 0; width: 10px; height: 380px;
    background: linear-gradient(135deg, var(--gold-zig) 25%, transparent 25%) 0 0 / 10px 10px,
                linear-gradient(45deg, var(--gold-zig) 25%, transparent 25%) 0 0 / 10px 10px; }
  .slide-panel { position: absolute; left: 667px; top: 0; width: 313px; height: 380px;
    background: linear-gradient(180deg, #d9ddd2 0%, #eeeeea 40%, #e4e2dc 100%); border-left: 3px solid var(--gold-zig); }
  .slide-panel .kicker { position: absolute; left: 22px; top: 30px; font-family: "Lobster", cursive; font-size: 28px; color: var(--brown); white-space: nowrap; }
  .slide-panel .big { position: absolute; left: 22px; top: 70px; font-family: "Bebas Neue", sans-serif; font-size: 38px; line-height: 38px; color: var(--brown);
    white-space: nowrap; transform: scaleX(0.86); transform-origin: left top; }
  .slide-panel .small { position: absolute; left: 22px; top: 114px; font-family: "Didact Gothic", sans-serif; font-size: 19px; line-height: 22px; color: var(--brown); white-space: nowrap; }
  .slide-panel .star { position: absolute; left: 152px; top: 152px; color: var(--teal-text); font-size: 18px; }
  .quote-badge { position: absolute; left: 108px; top: 266px; width: 94px; height: 94px; }
  .quote-badge span { position: absolute; inset: 0; display: flex; align-items: center; justify-content: center; text-align: center;
    font-family: "Lobster", cursive; font-size: 21px; line-height: 18px; color: var(--teal-text); }
  .slider-dots { position: absolute; left: 17px; top: 343px; display: flex; gap: 10px; }
  .slider-dots i { width: 21px; height: 21px; border-radius: 50%; background: rgba(255,255,255,0.55); border: 2px solid rgba(255,255,255,0.7); }
  .slider-dots i.is-active { background: var(--gold-zig); border-color: #f5f0dc; }

  .arrow { position: absolute; top: 328px; }

  .features { position: absolute; left: 0; top: 620px; width: 1200px; height: 300px; }
  .feature-text { position: absolute; font-family: "Didact Gothic", sans-serif; color: var(--ink); text-align: center; white-space: nowrap; }
  .feature-rates { left: 153px; top: 702px; width: 240px; font-size: 19px; line-height: 24px; }
  .feature-offers { left: 470px; top: 664px; width: 256px; font-size: 18px; color: #fff; }
  .feature-dream { left: 800px; top: 698px; width: 225px; font-size: 19px; line-height: 24px; text-align: right; }
  .feature-hire { left: 825px; top: 810px; width: 200px; font-family: "Bebas Neue", sans-serif; font-size: 40px; line-height: 40px; color: var(--brown); }

  .footer-cols { position: absolute; top: 945px; left: 130px; display: flex; }
  .footer-col { width: 327px; font-size: 15px; line-height: 18px; }
  .footer-col p { max-width: 285px; }
  .footer-col h2 { font-family: "Lobster", cursive; font-weight: 400; font-size: 22px; line-height: 28px; color: var(--sky); margin-bottom: 14px; }
  .footer-col p + p { margin-top: 18px; }

  .to-top { position: absolute; left: 560px; top: 1133px; }
  .copyright { position: absolute; left: 798px; top: 1150px; font-family: Arial, sans-serif; font-size: 12px; color: #5f8fc0; white-space: nowrap; }
</style>
</head>
<body>

<header>
  <div class="brand"><span class="brand-dot"></span><span class="brand-name">Brightfield Canopies</span></div>
  <nav class="main-nav">
    <a href="#" class="is-current">Home</a><span class="sep"></span>
    <a href="#">Faq</a><span class="sep"></span>
    <a href="#">Gallery</a><span class="sep"></span>
    <a href="#">Hire</a><span class="sep"></span>
    <a href="#">Contact Us</a>
  </nav>
</header>

<div class="rule" style="top:174px"></div>

<svg class="arrow" style="left:66px" width="28" height="82" viewBox="0 0 28 82"><polygon points="28,0 0,41 28,82 20,41" fill="var(--sky)"/></svg>
<svg class="arrow" style="left:1104px" width="28" height="82" viewBox="0 0 28 82"><polygon points="0,0 28,41 0,82 8,41" fill="var(--sky)"/></svg>

<section class="slider">
  <div class="slide-photo" role="img" aria-label="Photo of wedding guests gathered beside a large white stretch marquee in a garden"></div>
  <div class="slide-zig"></div>
  <div class="slide-panel">
    <div class="kicker">Contact us for a quote</div>
    <div class="big">YOU MIGHT BE PLEASANTLY</div>
    <div class="small">SURPRISED WITH OUR RATES!</div>
    <div class="star">*</div>
    <div class="quote-badge">
      <svg width="94" height="94" viewBox="0 0 94 94">
        <g fill="#fff">
          <circle cx="47" cy="47" r="40"/>
          <circle cx="47" cy="9" r="9"/><circle cx="47" cy="85" r="9"/><circle cx="9" cy="47" r="9"/><circle cx="85" cy="47" r="9"/>
          <circle cx="20" cy="20" r="9"/><circle cx="74" cy="20" r="9"/><circle cx="20" cy="74" r="9"/><circle cx="74" cy="74" r="9"/>
        </g>
      </svg>
      <span>Get<br>a<br>Quote</span>
    </div>
  </div>
  <div class="slider-dots"><i class="is-active"></i><i></i><i></i><i></i></div>
</section>

<div class="rule" style="top:565px"></div>
<div class="rule" style="top:570px"></div>

<svg class="features" viewBox="0 620 1200 300" width="1200" height="300">
  <polygon points="80,862 108,857 108,892 92,894 98,878" fill="var(--brown-dark)"/>
  <polygon points="1120,862 1090,857 1090,892 1108,894 1102,878" fill="var(--brown-dark)"/>
  <circle cx="273" cy="755" r="127" fill="var(--sky-fill)"/>
  <circle cx="273" cy="755" r="121" fill="none" stroke="#3b3b3b" stroke-dasharray="5 4" stroke-width="1"/>
  <g fill="var(--brown)">
    <rect x="166" y="800" width="214" height="4"/><rect x="172" y="809" width="202" height="4"/>
    <rect x="178" y="818" width="190" height="4"/><rect x="184" y="827" width="178" height="4"/>
  </g>
  <circle cx="925" cy="755" r="127" fill="var(--pink)"/>
  <circle cx="925" cy="755" r="121" fill="none" stroke="#3b3b3b" stroke-dasharray="5 4" stroke-width="1"/>
  <circle cx="598" cy="753" r="130" fill="none" stroke="#3b3b3b" stroke-dasharray="5 4" stroke-width="1"/>
  <circle cx="598" cy="753" r="124" fill="var(--teal-ring)"/>
  <circle cx="598" cy="753" r="117" fill="var(--sky-fill)"/>
  <rect x="510" y="700" width="176" height="172" rx="10" fill="#a88a73" opacity="0.55" role="img" aria-label="Illustration of a bride and groom holding a bouquet"/>
  <rect x="108" y="857" width="982" height="35" fill="var(--brown)"/>
  <polygon points="583,892 613,892 598,910" fill="var(--brown)"/>
</svg>

<div class="feature-text feature-rates">Check Our Rates<br>You might be surprised!</div>
<div class="feature-text feature-offers">Offers and Promotions</div>
<div class="feature-text feature-dream">Have you ever dreamed<br>of getting married by the<br>beach, the lake or in the<br>mountains?</div>
<div class="feature-text feature-hire">HIRE*US</div>

<footer>
  <div class="footer-cols">
    <div class="footer-col">
      <h2>Contact</h2>
      <p>12 Harbour View Rd,<br>Raglan, New Zealand</p>
      <p>+64 21 555 0142<br>hello@brightfieldcanopies.co.nz</p>
    </div>
    <div class="footer-col">
      <h2>About</h2>
      <p>We are a dedicated team working to take part in your dreamed event project. Brightfield Canopies is helping people build memories. Special occasions is worth celebrating.</p>
    </div>
    <div class="footer-col">
      <h2>Recent Tweets</h2>
      <p>2 hours ago : @BrightfieldCanopies Thank you for your service, it was fabulous!</p>
      <p>A day ago : New discount in Marquees!</p>
    </div>
  </div>
  <svg class="to-top" width="78" height="47" viewBox="0 0 78 47">
    <polygon points="39,0 78,47 0,47" fill="var(--brown)"/>
    <text x="40" y="38" text-anchor="middle" font-family="Lobster, cursive" font-size="20" fill="#fff">Up</text>
  </svg>
  <div class="copyright">© 2013 Brightfield Canopies All Rights Reserved</div>
</footer>

</body>
</html>
```